App Design for Restaurant App

We need a design for the new Mobile App for the Restaurant Velmo. See attachment for presentation sketches.
There are two attached files: File 2 shows the App in general and File 1 shows the five screens which need to be designed. Your work should contain the general color scheme, icons and layout proposal.
Updates
Hi Designers
There where several questions about the scope of the work. We are looking for a design for an App. The promotion website of the restaurant Velmo can be found under www.restaurant-velmo.example
There you will get an impression of the Corporate Identity used by the restaurant and you will also find the logo.
In the sketch there are several screens which don't need a design, e.g. the cover flow or video screen
please ask if you have any question
kind regards
Tobias
Industry/Entity Type
Restaurant
Look and feel
Each slider illustrates characteristics of the customer's brand and the style your logo design should communicate.

```html
<!DOCTYPE html>
<html lang="de">
<head>
<meta charset="utf-8">
<title>Restaurant Velmo – App Startseite</title>
<link rel="stylesheet" href="https://fonts.googleapis.com/css2?family=Source+Sans+3:wght@600;700&display=swap">
<style>
  :root {
    --stage: #2b2b2b;
    --screen-light: #f8f3c2;
    --screen-mid: #efe59a;
    --screen-edge: #e3d67a;
    --ink: #3b381b;
    --ink-soft: #55512c;
    --glint: #fbf7d6;
  }
  * { box-sizing: border-box; margin: 0; padding: 0; }
  html, body {
    width: 1129px;
    height: 1200px;
    overflow: hidden;
    background: var(--stage);
  }
  .app-screen {
    position: absolute;
    left: 195px;
    top: 50px;
    width: 738px;
    height: 1100px;
    background:
      radial-gradient(ellipse 70% 45% at 55% 28%, var(--screen-light) 0%, rgba(248,243,194,0) 70%),
      linear-gradient(180deg, var(--screen-edge) 0%, var(--screen-mid) 30%, var(--screen-mid) 75%, var(--screen-edge) 100%);
    font-family: "Source Sans 3", Arial, sans-serif;
    color: var(--ink);
  }
  .app-screen::after {
    content: "";
    position: absolute;
    left: 0; right: 0; bottom: 22px;
    height: 6px;
    background: linear-gradient(90deg, rgba(251,247,214,0) 0%, var(--glint) 50%, rgba(251,247,214,0) 100%);
  }
  .brand {
    position: absolute;
    top: 110px;
    left: 0;
    width: 100%;
    text-align: center;
  }
  .brand-dot {
    display: block;
    width: 150px;
    height: 150px;
    margin: 0 auto 34px;
    border-radius: 50%;
    background: var(--ink);
  }
  .brand-name {
    font-weight: 600;
    font-size: 42px;
    line-height: 44px;
    letter-spacing: 5px;
    text-transform: uppercase;
    color: var(--ink);
  }
  .menu-grid {
    position: absolute;
    top: 460px;
    left: 30px;
    width: 678px;
    display: grid;
    grid-template-columns: repeat(3, 1fr);
    row-gap: 92px;
    list-style: none;
  }
  .menu-item {
    display: flex;
    flex-direction: column;
    align-items: center;
    gap: 14px;
  }
  .menu-icon {
    width: 94px;
    height: 94px;
    color: var(--ink);
  }
  .menu-label {
    font-weight: 700;
    font-size: 27px;
    line-height: 30px;
    color: var(--ink-soft);
  }
</style>
</head>
<body>
<main class="app-screen">
  <header class="brand">
    <span class="brand-dot"></span>
    <h1 class="brand-name">Restaurant<br>Velmo</h1>
  </header>

  <ul class="menu-grid">
    <li class="menu-item">
      <svg class="menu-icon" viewBox="0 0 48 48" aria-hidden="true">
        <circle cx="24" cy="24" r="21" fill="currentColor"/>
        <circle cx="24" cy="24" r="17.5" fill="none" stroke="#efe59a" stroke-width="1.5"/>
        <circle cx="26" cy="14" r="2.6" fill="#efe59a"/>
        <path d="M21 20h7l-3 14h3v2h-8l3-14h-2z" fill="#efe59a"/>
      </svg>
      <span class="menu-label">Aktuell</span>
    </li>
    <li class="menu-item">
      <svg class="menu-icon" viewBox="0 0 48 48" aria-hidden="true">
        <rect x="5" y="15" width="27" height="20" rx="2" fill="currentColor"/>
        <path d="M32 22l11-5v16l-11-5z" fill="currentColor"/>
      </svg>
      <span class="menu-label">Webcam</span>
    </li>
    <li class="menu-item">
      <svg class="menu-icon" viewBox="0 0 48 48" aria-hidden="true">
        <path d="M24 4L2 24h5v20h13V32h8v12h13V24h5L36 15V7h-5v4z" fill="currentColor"/>
      </svg>
      <span class="menu-label">Restaurant</span>
    </li>
    <li class="menu-item">
      <svg class="menu-icon" viewBox="0 0 48 48" aria-hidden="true">
        <path d="M20 4l-4 4 3 3-6 7c-3-1-6 0-8 2l16 16c2-2 3-5 2-8l7-6 3 3 4-4z" fill="currentColor"/>
        <path d="M16 28L38 44" stroke="currentColor" stroke-width="3" stroke-linecap="round"/>
      </svg>
      <span class="menu-label">Events</span>
    </li>
    <li class="menu-item">
      <svg class="menu-icon" viewBox="0 0 48 48" aria-hidden="true">
        <rect x="6" y="4" width="36" height="40" fill="currentColor"/>
        <g fill="#efe59a">
          <rect x="9" y="7" width="30" height="6"/>
          <rect x="9" y="16" width="6" height="5"/><rect x="17" y="16" width="6" height="5"/><rect x="25" y="16" width="6" height="5"/><rect x="33" y="16" width="6" height="5"/>
          <rect x="9" y="24" width="6" height="5"/><rect x="17" y="24" width="6" height="5"/><rect x="25" y="24" width="6" height="5"/><rect x="33" y="24" width="6" height="5"/>
          <rect x="9" y="32" width="6" height="5"/><rect x="17" y="32" width="6" height="5"/><rect x="25" y="32" width="6" height="5"/><rect x="33" y="32" width="6" height="5"/>
        </g>
      </svg>
      <span class="menu-label">Reservation</span>
    </li>
    <li class="menu-item">
      <svg class="menu-icon" viewBox="0 0 48 48" aria-hidden="true">
        <rect x="8" y="3" width="32" height="42" fill="currentColor"/>
        <g fill="#efe59a">
          <rect x="12" y="7" width="24" height="4"/><rect x="12" y="14" width="24" height="4"/>
          <rect x="12" y="21" width="24" height="4"/><rect x="12" y="28" width="24" height="4"/>
          <rect x="12" y="35" width="24" height="4"/>
        </g>
      </svg>
      <span class="menu-label">Menükarte</span>
    </li>
    <li class="menu-item">
      <svg class="menu-icon" viewBox="0 0 48 48" aria-hidden="true">
        <path d="M17 10h14l3 5h8a3 3 0 0 1 3 3v22a3 3 0 0 1-3 3H6a3 3 0 0 1-3-3V18a3 3 0 0 1 3-3h8z" fill="currentColor"/>
        <circle cx="24" cy="28" r="9" fill="#efe59a"/>
        <circle cx="24" cy="28" r="6.5" fill="currentColor"/>
      </svg>
      <span class="menu-label">Galerie</span>
    </li>
    <li class="menu-item">
      <svg class="menu-icon" viewBox="0 0 48 48" aria-hidden="true">
        <path d="M42 5L5 22l17 3 3 18z" fill="currentColor"/>
      </svg>
      <span class="menu-label">Anfahrt</span>
    </li>
    <li class="menu-item">
      <svg class="menu-icon" viewBox="0 0 48 48" aria-hidden="true">
        <path d="M2 9h3v30h17c1 0 2 1 2 2 0-1 1-2 2-2h17V9h3v34H2z" fill="currentColor"/>
        <path d="M7 6c6 0 12 1 16 4v29c-4-3-10-4-16-4zM41 6c-6 0-12 1-16 4v29c4-3 10-4 16-4z" fill="none" stroke="currentColor" stroke-width="2.5"/>
      </svg>
      <span class="menu-label">Gästebuch</span>
    </li>
  </ul>
</main>
</body>
</html>
```